Brightwell Dwellings

Design a stylish Business card- we would like a businness card design that suits plastic business cards. Our card needs to show that we are tech savy and technology based so the design is crucial.

Target Market(s)

22-40

Industry/Entity Type

Plastic

Requirements
Must have
• attached is our logo. also double sided card would be nice.
my details

Callum Fenwright
Director
0461927345
www.brightwelldwellings.com.au
17 Marlow Crest Avenue, West Perth

```html
<!DOCTYPE html>
<html lang="en">
<head>
<meta charset="utf-8">
<title>Brightwell Dwellings – Business Card</title>
<link href="https://fonts.googleapis.com/css2?family=Barlow:wght@400;500;600&display=swap" rel="stylesheet">
<style>
  :root {
    --page-bg: #e9e7e4;
    --card-dark: #0f1214;
    --card-mid: #1e2427;
    --accent-blue: #3ba9d8;
    --accent-copper: #a8764e;
    --text-light: #cfd3d5;
    --text-muted: #9aa1a5;
    --tagline: #dfe2e3;
  }
  * { margin: 0; padding: 0; box-sizing: border-box; }
  html, body {
    width: 1178px;
    height: 1200px;
    overflow: hidden;
    background: var(--page-bg);
    font-family: "Barlow", Arial, sans-serif;
  }
  .sheet {
    position: relative;
    width: 1178px;
    height: 1200px;
  }
  .card {
    position: absolute;
    left: 159px;
    width: 860px;
    height: 470px;
    border-radius: 28px;
    background: linear-gradient(160deg, var(--card-mid) 0%, var(--card-dark) 55%, #0b0d0e 100%);
    box-shadow: 0 14px 30px rgba(0,0,0,0.25);
    overflow: hidden;
  }
  .card--details { top: 90px; }
  .card--brand { top: 640px; }

  /* details side */
  .details {
    position: absolute;
    left: 70px;
    top: 225px;
    display: flex;
    align-items: flex-start;
    gap: 26px;
  }
  .details__mark {
    width: 140px;
    height: 140px;
    border: 4px solid var(--accent-copper);
    border-radius: 10px;
    margin-top: 18px;
  }
  .details__name {
    color: var(--accent-blue);
    font-size: 34px;
    font-weight: 600;
    letter-spacing: 2px;
    text-transform: uppercase;
    line-height: 1;
  }
  .details__role {
    color: var(--text-muted);
    font-size: 22px;
    letter-spacing: 3px;
    margin-top: 8px;
  }
  .details__contact {
    list-style: none;
    margin-top: 24px;
    color: var(--text-light);
    font-size: 27px;
    line-height: 1.12;
  }

  /* brand side */
  .brand {
    position: absolute;
    left: 0;
    right: 0;
    top: 150px;
    text-align: center;
  }
  .brand__tagline {
    color: var(--tagline);
    font-size: 30px;
    font-weight: 500;
    margin-bottom: 20px;
    padding-left: 150px;
  }
  .brand__lockup {
    display: inline-flex;
    align-items: center;
    gap: 28px;
  }
  .brand__square {
    width: 96px;
    height: 96px;
    border: 4px solid var(--accent-copper);
    border-radius: 8px;
  }
  .brand__name {
    color: var(--accent-blue);
    font-size: 70px;
    font-weight: 600;
    letter-spacing: 1px;
    line-height: 1;
  }
</style>
</head>
<body>
<main class="sheet">
  <section class="card card--details" aria-label="Business card, contact side">
    <div class="details">
      <div class="details__mark" aria-hidden="true"></div>
      <div class="details__text">
        <p class="details__name">Callum Fenwright</p>
        <p class="details__role">Director</p>
        <ul class="details__contact">
          <li>0461927345</li>
          <li>17 Marlow Crest Avenue, West Perth</li>
          <li>www.brightwelldwellings.com.au</li>
        </ul>
      </div>
    </div>
  </section>

  <section class="card card--brand" aria-label="Business card, brand side">
    <div class="brand">
      <p class="brand__tagline">Smart Living Starts With One Tap</p>
      <div class="brand__lockup">
        <p class="brand__name">Brightwell Dwellings</p>
        <div class="brand__square" aria-hidden="true"></div>
      </div>
    </div>
  </section>
</main>
</body>
</html>
```